Fiber Optic Internet flyer promotion Winter 2016-2017

I am looking for a marketing flyer that will not be folded, single sided that will advertise a Fiber Optic internet promotion that we are currently running.

The design should be clean, flow well, quickly grab attention, and if a very few short seconds list what the promotion is, and direct them to contact us.

It needs to list a few features of the promotion, but does not need to be in this order and should flow well with the flyer
1.) Fiber Optic Internet
2.) 100 Mbits for $140 /month or 150 Mbits for $190 /month
3.) Free construction cost up to $10,000, limited funds available.
4.) Limited time offer. Must commit before funds run out.

(555) 274-3916, www.kelvoranet.example

Target Market(s)

Small to large business

Industry/Entity Type

Internet Service Provider

Requirements
Must have
• Eye catching appeal. Quickly convey the message of the promotion and our company name and phone number.
Should not have
• Our company is primarily a wireless ISP. This promotion is all about Fiber Optic. I do not want to draw attention to the "wireless" portion of our business with this flyer.

```html
<!DOCTYPE html>
<html lang="en">
<head>
<meta charset="utf-8">
<title>Kelvora Net – Fiber Optic Internet Flyer</title>
<link rel="stylesheet" href="https://fonts.googleapis.com/css2?family=Crimson+Text:wght@600;700&family=Lato:wght@400;700&display=swap">
<style>
  :root {
    --backdrop: #d4d4d6;
    --paper: #ececee;
    --paper-light: #f6f6f7;
    --brand-blue: #3e4f95;
    --brand-blue-deep: #2c3870;
    --headline-blue: #3b4a8c;
    --offer-red: #b3202e;
    --ink: #2a2a2a;
    --white: #ffffff;
  }
  * { box-sizing: border-box; margin: 0; padding: 0; }
  html, body { width: 872px; height: 1200px; overflow: hidden; }
  body { background: var(--backdrop); position: relative; }

  .flyer {
    position: absolute;
    left: 13px; top: 38px;
    width: 676px; height: 899px;
    transform: scale(1.25);
    transform-origin: 0 0;
    background: linear-gradient(180deg, var(--paper-light), var(--paper));
    font-family: "Crimson Text", Georgia, serif;
    overflow: hidden;
  }

  .hero {
    position: absolute; left: 0; top: 0;
    width: 676px; height: 287px;
    background:
      radial-gradient(ellipse at 60% 40%, rgba(255,240,230,.85), rgba(255,240,230,0) 45%),
      linear-gradient(100deg, #7a6570 0%, #a58f9b 35%, #b9a7b8 55%, #5a3e58 85%, #2d1f35 100%);
  }
  .hero-brand {
    position: absolute; right: 22px; top: 130px;
    display: flex; align-items: center; gap: 8px;
    color: var(--brand-blue);
    font-weight: 700; font-size: 30px; letter-spacing: 1px;
  }
  .hero-brand .mark {
    width: 14px; height: 14px; border-radius: 50%; background: var(--brand-blue);
  }

  .title-strip {
    position: absolute; left: 0; top: 287px; width: 676px; height: 105px;
    background: var(--paper-light);
  }
  .title-banner { position: absolute; left: 0; top: 17px; }
  .title-banner text {
    font-family: "Crimson Text", Georgia, serif;
    font-weight: 700; font-size: 34px; fill: var(--white);
  }

  .pricing {
    position: absolute; left: 0; top: 394px; width: 676px; height: 113px;
    background: var(--brand-blue);
    color: var(--white);
    border-bottom: 15px solid var(--brand-blue-deep);
    height: 128px;
  }
  .pricing .plan {
    position: absolute; left: 20px;
    font-weight: 700; font-size: 31px; line-height: 1;
  }
  .pricing .plan-a { top: 13px; }
  .pricing .plan-b { top: 70px; }
  .pricing .or {
    position: absolute; left: 542px; top: 44px;
    font-weight: 700; font-size: 29px;
  }

  .construction {
    position: absolute; left: 0; top: 545px; width: 676px;
    text-align: center; color: var(--headline-blue);
    font-weight: 700; font-size: 41px; line-height: 54px;
  }
  .construction .spaced { letter-spacing: 4.5px; display: block; }

  .offer { position: absolute; left: 41px; top: 746px; }
  .offer-title { color: var(--offer-red); font-weight: 700; font-size: 30px; line-height: 1; }
  .offer-note { color: var(--ink); font-weight: 600; font-size: 19px; margin-top: 4px; }

  .footer-brand {
    position: absolute; right: 30px; top: 790px;
    display: flex; align-items: center; gap: 6px;
    color: var(--brand-blue);
    font-weight: 700; font-size: 22px; letter-spacing: .5px;
  }
  .footer-brand .mark { width: 10px; height: 10px; border-radius: 50%; background: var(--brand-blue); }

  .contact-bar {
    position: absolute; left: 0; top: 855px; width: 676px; height: 44px;
    background: var(--brand-blue); color: var(--white);
    font-family: "Lato", Arial, sans-serif; font-size: 14px;
    display: flex; align-items: center; justify-content: space-between;
    padding: 0 30px 0 34px;
  }
  .contact-item { display: flex; align-items: center; gap: 10px; }
  .contact-item svg { width: 20px; height: 20px; }
</style>
</head>
<body>
  <main class="flyer">
    <section class="hero" role="img" aria-label="Photo of a fiber optic cable with colorful tubes and glowing strands of light">
      <div class="hero-brand"><span class="mark"></span>KELVORA NET</div>
    </section>

    <section class="title-strip">
      <svg class="title-banner" width="500" height="70" viewBox="0 0 500 70">
        <polygon points="0,0 420,0 498,68 0,68" fill="var(--brand-blue)"/>
        <text x="20" y="46">Fiber Optic Internet</text>
      </svg>
    </section>

    <section class="pricing">
      <p class="plan plan-a">100 Mbits for $140 /month</p>
      <p class="plan plan-b">150 Mbits for $190 /month</p>
      <p class="or">(or)</p>
    </section>

    <h2 class="construction">
      <span class="spaced">Free construction</span>
      <span class="spaced">cost up to $10,000,</span>
      <span>limited funds available.</span>
    </h2>

    <div class="offer">
      <p class="offer-title">Limited time offer!!</p>
      <p class="offer-note">Must commit before funds run out.</p>
    </div>

    <div class="footer-brand"><span class="mark"></span>KELVORA NET</div>

    <footer class="contact-bar">
      <div class="contact-item">
        <svg viewBox="0 0 20 20" aria-hidden="true">
          <circle cx="10" cy="10" r="10" fill="#e8e9f0"/>
          <rect x="7" y="4.5" width="6" height="11" rx="1.2" fill="var(--brand-blue)"/>
          <rect x="8" y="6" width="4" height="7" fill="#e8e9f0"/>
        </svg>
        <span>(555) 274-3916</span>
      </div>
      <div class="contact-item">
        <svg viewBox="0 0 20 20" aria-hidden="true">
          <circle cx="10" cy="10" r="10" fill="#e8e9f0"/>
          <circle cx="10" cy="10" r="5.5" fill="none" stroke="var(--brand-blue)" stroke-width="1.2"/>
          <ellipse cx="10" cy="10" rx="2.4" ry="5.5" fill="none" stroke="var(--brand-blue)" stroke-width="1"/>
          <line x1="4.5" y1="10" x2="15.5" y2="10" stroke="var(--brand-blue)" stroke-width="1"/>
        </svg>
        <span>www.kelvoranet.example</span>
      </div>
    </footer>
  </main>
</body>
</html>
```